Vemarok Contracting Folder

Creating a design for the cover of our folders that we pass to our customers

Want to keep the same look as our colors and fonts as attached

```html
<!DOCTYPE html>
<html lang="en">
<head>
<meta charset="UTF-8">
<title>Vemarok Contracting Folder Cover</title>
<link rel="stylesheet" href="https://fonts.googleapis.com/css2?family=Questrial&family=Didact+Gothic&display=swap">
<style>
  :root {
    --backdrop: #b1c3ec;
    --paper: #ffffff;
    --brand-blue: #1414b4;
    --navy: #174a72;
    --sky-top: #133f66;
    --sky-bottom: #1b5a8a;
    --facade: #b9b48c;
    --sun-yellow: #f9d335;
    --ink-blue: #1f3a93;
    --link-blue: #3a5fd0;
    --lilac: #b0b3e0;
    --white: #ffffff;
  }
  * { margin: 0; padding: 0; box-sizing: border-box; }
  html, body {
    width: 1200px; height: 791px; overflow: hidden;
    background: var(--backdrop);
  }
  .folder-cover {
    position: absolute; left: 427px; top: 48px;
    width: 346px; height: 695px;
    background: var(--paper);
    font-family: "Questrial", "Didact Gothic", sans-serif;
    overflow: hidden;
  }
  .cover-shapes { position: absolute; inset: 0; width: 100%; height: 100%; }
  .brand-name {
    position: absolute; left: 0; right: 0; top: 18px;
    text-align: center; font-size: 58px; line-height: 64px;
    color: var(--brand-blue); letter-spacing: 2px;
  }
  .brand-tagline {
    position: absolute; left: 0; right: 0; top: 86px;
    text-align: center; font-size: 14px; letter-spacing: 2.2px;
    color: var(--lilac);
  }
  .headline { position: absolute; left: 38px; top: 134px; color: var(--white); }
  .headline-kicker { font-size: 15px; line-height: 18px; letter-spacing: 0.3px; }
  .headline-main { font-size: 32px; line-height: 32px; letter-spacing: 0.5px; margin-top: 4px; }
  .services {
    position: absolute; top: 516px; color: var(--ink-blue);
    font-size: 15.5px; line-height: 20px; white-space: nowrap;
  }
  .services .line-one { margin-left: 81px; }
  .services .line-two { margin-left: 73px; }
  .since-badge {
    position: absolute; left: 22px; top: 610px; width: 80px;
    text-align: center; color: var(--white);
  }
  .since-label { font-size: 12px; line-height: 14px; }
  .since-year { font-size: 21px; line-height: 24px; }
  .contact {
    position: absolute; left: 125px; top: 615px;
    font-size: 7.8px; line-height: 10.5px; color: var(--ink-blue);
    font-weight: bold; white-space: nowrap;
  }
  .website {
    position: absolute; right: 33px; top: 649px;
    font-size: 11px; font-weight: bold; letter-spacing: 0.4px;
    color: var(--ink-blue);
  }
  .website .domain { color: var(--link-blue); }
</style>
</head>
<body>
  <main class="folder-cover">
    <svg class="cover-shapes" viewBox="0 0 433 869" preserveAspectRatio="none" aria-hidden="false">
      <defs>
        <linearGradient id="skyFacade" x1="0" y1="0" x2="1" y2="1">
          <stop offset="0" stop-color="var(--sky-top)"/>
          <stop offset="0.55" stop-color="var(--sky-bottom)"/>
          <stop offset="0.8" stop-color="var(--facade)"/>
          <stop offset="1" stop-color="#8f8a63"/>
        </linearGradient>
      </defs>
      <polygon class="yellow-band" points="230,252 433,252 433,726 21,726" fill="var(--sun-yellow)"/>
      <polygon class="building-photo" role="img" aria-label="Photo of a tall apartment building facade against a deep blue sky, seen from below"
               points="0,140 415,140 206,614 0,614" fill="url(#skyFacade)"/>
      <circle class="badge-disc" cx="77" cy="798" r="50" fill="var(--navy)"/>
      <circle class="badge-dot-yellow" cx="30" cy="769" r="18" fill="var(--sun-yellow)"/>
      <circle class="badge-dot-lilac" cx="44" cy="749" r="10" fill="var(--lilac)"/>
    </svg>

    <h1 class="brand-name">VEMAROK</h1>
    <p class="brand-tagline">Painting &amp; Contracting</p>

    <div class="headline">
      <p class="headline-kicker">PROFESSIONALS</p>
      <p class="headline-main">YOU CAN<br>TRUST!</p>
    </div>

    <div class="services">
      <p class="line-one">INTERIOR &amp; EXTERIOR PAINTING</p>
      <p class="line-two">RESIDENTIAL &amp; COMMERCIAL</p>
    </div>

    <div class="since-badge">
      <p class="since-label">SINCE</p>
      <p class="since-year">1960</p>
    </div>

    <address class="contact" style="font-style: normal;">
      4120 Larkspur Ave. Fairview, VA 22410<br>
      Phone: (555) 214.0380 &bull; Fax: (555) 214.0391
    </address>

    <p class="website">WWW.<span class="domain">VEMAROKPAINTING</span>.COM</p>
  </main>
</body>
</html>
```